Corporate Business Card

Very professional, Modern, Not to busy, include phone address email, website
(253) 555-0174, 61807 19th Street N, Kent, WA 98517, marcus@kestrelbayholding.com, brelvanindustries.com

Target Market(s)

Manufacturing

Industry/Entity Type

Aero, machining, manufacturing, Off road racing

Contact Information for Business Card

Phone, address email, website

```html
<!DOCTYPE html>
<html lang="en">
<head>
<meta charset="utf-8">
<title>Brelvan Industries – Business Card</title>
<link href="https://fonts.googleapis.com/css2?family=Exo+2:wght@400;600&display=swap" rel="stylesheet">
<style>
  :root {
    --bg: #d9d9d9;
    --red: #d2232a;
    --navy: #16356b;
    --white: #ffffff;
    --ghost: #e6e6e6;
    --ink: #1b3470;
  }
  * { margin: 0; padding: 0; box-sizing: border-box; }
  html, body {
    width: 1200px; height: 900px; overflow: hidden;
    background: var(--bg);
    font-family: "Exo 2", sans-serif;
  }
  .card {
    position: absolute;
    left: 270px;
    width: 660px; height: 377px;
    border-radius: 30px;
    overflow: hidden;
    box-shadow: 0 6px 16px rgba(0,0,0,0.25);
  }
  .card--front {
    top: 50px;
    background: linear-gradient(160deg, var(--red) 0%, #7a2a4f 45%, var(--navy) 85%);
  }
  .card--back {
    top: 470px;
    background: var(--white);
  }
  .wordmark {
    position: absolute;
    font-weight: 600;
    line-height: 1;
  }
  .wordmark__name {
    display: block;
    font-size: 62px;
    letter-spacing: 3px;
    text-transform: uppercase;
  }
  .wordmark__sub {
    display: block;
    font-size: 22px;
    letter-spacing: 2px;
    text-align: right;
    margin-top: 4px;
  }
  .wordmark__rule {
    display: block;
    height: 2px;
    width: 60%;
    margin-top: 10px;
  }
  .card--front .wordmark { left: 170px; top: 130px; color: var(--white); }
  .card--front .wordmark__rule { background: var(--white); }
  .card--front .wordmark--ghost { left: 330px; top: 170px; color: rgba(255,255,255,0.1); }
  .card--front .wordmark--ghost .wordmark__rule { background: rgba(255,255,255,0.1); }

  .card--back .wordmark { left: 60px; top: 110px; color: var(--navy); }
  .card--back .wordmark__name { font-size: 50px; }
  .card--back .wordmark__sub { font-size: 19px; }
  .card--back .wordmark__rule { background: var(--navy); }
  .card--back .wordmark--ghost { left: 340px; top: 60px; color: var(--ghost); }
  .card--back .wordmark--ghost .wordmark__name { font-size: 66px; }
  .card--back .wordmark--ghost .wordmark__sub { font-size: 22px; }
  .card--back .wordmark--ghost .wordmark__rule { background: var(--ghost); }

  .contact {
    position: absolute;
    left: 60px; bottom: 40px;
    list-style: none;
    color: var(--ink);
    font-size: 17px;
    font-weight: 400;
  }
  .contact__item {
    display: flex; align-items: center; gap: 10px;
    line-height: 1.5;
  }
  .contact__icon { width: 16px; height: 16px; flex: none; }
  .address {
    position: absolute;
    right: 50px; top: 180px;
    text-align: right;
    color: var(--ink);
    font-size: 17px;
    line-height: 1.4;
    font-style: normal;
  }
</style>
</head>
<body>

<section class="card card--front" aria-label="Card front">
  <div class="wordmark wordmark--ghost" aria-hidden="true">
    <span class="wordmark__name">Brelvan</span>
    <span class="wordmark__sub">Industries</span>
    <span class="wordmark__rule"></span>
  </div>
  <div class="wordmark">
    <span class="wordmark__name">Brelvan</span>
    <span class="wordmark__sub">Industries</span>
    <span class="wordmark__rule"></span>
  </div>
</section>

<section class="card card--back" aria-label="Card back">
  <div class="wordmark wordmark--ghost" aria-hidden="true">
    <span class="wordmark__name">Brelvan</span>
    <span class="wordmark__sub">Industries</span>
    <span class="wordmark__rule"></span>
  </div>
  <div class="wordmark">
    <span class="wordmark__name">Brelvan</span>
    <span class="wordmark__sub">Industries</span>
    <span class="wordmark__rule"></span>
  </div>

  <address class="address">
    61807 19th Street N<br>
    Kent, WA 98517
  </address>

  <ul class="contact">
    <li class="contact__item">
      <svg class="contact__icon" viewBox="0 0 16 16" aria-hidden="true">
        <path fill="#d2232a" d="M3.5 1.5l2.5 3-1.5 1.5c.8 1.8 2.2 3.2 4 4l1.5-1.5 3 2.5-1.5 2.5C6.5 13.5 2.5 9.5 1 3z"/>
      </svg>
      (253) 555-0174
    </li>
    <li class="contact__item">
      <svg class="contact__icon" viewBox="0 0 16 16" aria-hidden="true">
        <rect x="1" y="3" width="14" height="10" fill="#d2232a"/>
        <path d="M1.5 3.5L8 9l6.5-5.5" fill="none" stroke="#fff" stroke-width="1.2"/>
      </svg>
      marcus@kestrelbayholding.com
    </li>
    <li class="contact__item">
      <svg class="contact__icon" viewBox="0 0 16 16" aria-hidden="true">
        <g fill="none" stroke="#d2232a" stroke-width="1.4">
          <circle cx="8" cy="8" r="6.5"/>
          <ellipse cx="8" cy="8" rx="2.8" ry="6.5"/>
          <path d="M1.5 8h13M2.5 4.8h11M2.5 11.2h11"/>
        </g>
      </svg>
      www.brelvanindustries.com
    </li>
  </ul>
</section>

</body>
</html>
```